Retractable Banner Design featuring Key Product for Beauty Trade Show (Eyelash Extensions)

We're a beauty/nail supply company that specializes in products used in professional nail salons. The key product for this design is "Eyelash Extensions".

We will be exhibiting in a trade show and are looking for a free-standing Retractable Banner Design that will be displayed at the front of our booth. The goal of the banner will be to display key products that are high in demand with our customers. The banner will be used to attract attention and highlight key selling points of these popular products. We would like the banner to be focused on the product title, image and key points, with a beauty/model/pattern background to create a professional appearance.

Target Market(s)

Nail Salons

Industry/Entity Type

Beauty

Requirements
Nice to have
• Eyelash model or close up of eyelash product in use.

```html
<!DOCTYPE html>
<html lang="en">
<head>
<meta charset="utf-8">
<title>SilkGaze Eyelash Extensions Banner</title>
<link rel="stylesheet" href="https://fonts.googleapis.com/css2?family=Montserrat:wght@400;500;700;800&family=Playfair+Display:ital,wght@1,700;1,800&display=swap">
<style>
:root{
  --lime:#dfe88f;
  --lime-light:#eef3bd;
  --purple:#7a2a8c;
  --purple-soft:#a98ad6;
  --lavender:#d9ccef;
  --lavender-light:#ece5f8;
  --ink:#3a3a3a;
  --grey:#6b6b6b;
  --orange:#f7a21b;
  --coral:#f08a7e;
  --white:#ffffff;
}
*{margin:0;padding:0;box-sizing:border-box}
html,body{width:831px;height:1200px;overflow:hidden;background:var(--white)}
.banner{position:relative;width:831px;height:1200px;overflow:hidden;background:var(--white);font-family:"Montserrat",sans-serif}
.banner-shapes{position:absolute;inset:0}
.brand{position:absolute;top:62px;left:0;width:100%;text-align:center}
.brand-name{font-family:"Montserrat",sans-serif;font-weight:800;font-size:84px;letter-spacing:-2px;color:var(--ink);line-height:1}
.brand-tag{display:block;margin:2px 0 0 260px;font-size:22px;font-weight:500;color:var(--ink)}
.product-title{position:absolute;top:196px;width:100%;text-align:center;font-family:"Playfair Display",serif;font-style:italic;font-weight:800;font-size:58px;color:var(--purple)}
.model-photo{position:absolute;left:0;top:0;width:831px;height:1200px}
.key-heading{position:absolute;top:708px;width:100%;text-align:center;font-weight:800;font-size:96px;color:var(--purple);letter-spacing:-1px}
.features{position:absolute;top:838px;left:110px;width:640px;display:grid;grid-template-columns:1fr 1fr;column-gap:50px;row-gap:26px}
.feature{border-left:3px solid var(--purple-soft);padding-left:12px}
.feature-title{font-weight:700;font-size:19px;color:var(--purple)}
.feature-text{font-size:13px;line-height:1.35;color:var(--grey);margin-top:3px}
.quantity{position:absolute;left:80px;top:985px;width:160px;height:160px;border-radius:50%;background:var(--orange);display:flex;flex-direction:column;justify-content:center;align-items:center;text-align:center;color:var(--white)}
.quantity-label{font-weight:800;font-size:24px}
.quantity-text{font-size:12px;font-weight:500;line-height:1.3;margin-top:4px}
.product-photo{position:absolute;left:265px;top:990px;width:490px;height:180px;border-radius:6px;background:linear-gradient(180deg,#f4f2f6,#cfc9d6);box-shadow:0 4px 12px rgba(0,0,0,.15)}
</style>
</head>
<body>
<main class="banner">
  <svg class="banner-shapes" width="831" height="1200" viewBox="0 0 831 1200" aria-hidden="true">
    <defs>
      <linearGradient id="topBg" x1="0" y1="0" x2="0" y2="1">
        <stop offset="0" stop-color="#d6e27c"/><stop offset="1" stop-color="#eef3bd"/>
      </linearGradient>
      <linearGradient id="bottomBg" x1="0" y1="0" x2="1" y2="0">
        <stop offset="0" stop-color="#c9b6ec"/><stop offset="1" stop-color="#ece5f8"/>
      </linearGradient>
    </defs>
    <rect width="831" height="340" fill="url(#topBg)"/>
    <path d="M0 960 C180 920 380 1010 580 975 C700 955 780 930 831 920 L831 1200 L0 1200 Z" fill="url(#bottomBg)"/>
    <path d="M0 1030 C200 1000 420 1080 831 1010 L831 1200 L0 1200 Z" fill="#b9a2e4" opacity=".45"/>
  </svg>

  <svg class="model-photo" width="831" height="1200" viewBox="0 0 831 1200" role="img" aria-label="Close-up photograph of a model's face showing long, full eyelash extensions">
    <defs>
      <linearGradient id="skin" x1="0" y1="0" x2="1" y2="1">
        <stop offset="0" stop-color="#3b2a26"/><stop offset=".35" stop-color="#d9ad95"/><stop offset="1" stop-color="#f0d3c2"/>
      </linearGradient>
    </defs>
    <path d="M0 330 C200 300 420 360 600 320 C700 300 780 290 831 300 L831 600 C700 660 520 640 380 672 C240 700 100 690 0 660 Z" fill="url(#skin)"/>
    <path d="M0 560 C60 600 100 650 150 680 C90 690 40 680 0 670 Z" fill="var(--coral)"/>
    <path d="M620 600 C700 590 780 580 831 560 L831 640 C760 660 700 660 620 600 Z" fill="var(--purple-soft)"/>
    <path d="M0 300 C120 300 160 330 180 340 C120 330 60 340 0 360 Z" fill="var(--purple-soft)"/>
  </svg>

  <header class="brand">
    <div class="brand-name">SilkGaze</div>
    <span class="brand-tag">Professional</span>
  </header>
  <h1 class="product-title">Eyelash Extensions</h1>

  <h2 class="key-heading">Key Points:</h2>
  <section class="features">
    <div class="feature"><div class="feature-title">Professional Falsies</div><p class="feature-text">Create beautiful and eye-opening appearances</p></div>
    <div class="feature"><div class="feature-title">Long-Lasting</div><p class="feature-text">Delicate overlapping hairs create the most authentic look</p></div>
    <div class="feature"><div class="feature-title">Handmade Perfection</div><p class="feature-text">Individually hand made with extreme attention to detail</p></div>
    <div class="feature"><div class="feature-title">Knot-Free Flares</div><p class="feature-text">Each tray holds 56 individual flares with a dramatic C-curl</p></div>
  </section>

  <div class="product-photo" role="img" aria-label="Product photograph of eyelash extension trays with rows of individual lash flares"></div>
  <div class="quantity">
    <span class="quantity-label">Quantity:</span>
    <span class="quantity-text">200 Trays Total<br>10 Boxes Each</span>
  </div>
</main>
</body>
</html>
```